White Paper and One-Page Advertisement for TELVARIS-QP

I need both documents to be better formatted and designed so they look professional, not something someone with mediocre word skills put together. They will go out to 1000s of industry professionals, and they need to look sharp. I need them to have my company's color palate logo, and branding on it similar to how it is now, but better. Please do not change any of the written content, but it can be arranged in any other format you think is better. Smart art and things i've already used can be omitted in favor of better designs. The developer is free to use their creativity. White paper should not be longer than the three pages unless necessary.

Target Market(s)

Life Sciences supply chain professionals

Colors
33b8a4
0592cd
9bcb3c
fbee3e
3277b5

Requirements
Must have
• Must be professional looking and not look like something done in word. Please use the color palate as seen on the documents.
Should not have
• Any changes to the written content.

```html
<!DOCTYPE html>
<html lang="en">
<head>
<meta charset="utf-8">
<title>Changing Pharma's Paradigm of Waste – White Paper</title>
<link href="https://fonts.googleapis.com/css2?family=Oswald:wght@500;700&family=Roboto+Condensed:wght@400;700&family=Roboto:wght@400;700&display=swap" rel="stylesheet">
<style>
  :root{
    --bg:#ececec;
    --teal:#33b8a4;
    --blue:#0592cd;
    --green:#9bcb3c;
    --yellow:#fbee3e;
    --navy:#3277b5;
    --title-teal:#2e86a6;
    --deep-teal:#3a9bb0;
    --sky:#7ccbdc;
    --pale-sky:#b9e1ea;
    --grey-light:#8e8e8e;
    --grey-dark:#555;
    --ink:#444;
    --stat-green:#8bbf3c;
    --stat-olive:#c9bf3a;
    --stat-teal:#1a9a7c;
    --stat-sky:#7ccbdc;
    --stat-foot:#e3e6e0;
    --summary-bg:#5aaec0;
    --sub-green:#6fb43a;
  }
  *{margin:0;padding:0;box-sizing:border-box}
  html,body{width:1200px;height:900px;overflow:hidden;background:var(--bg)}
  .spread{position:relative;width:1200px;height:900px}
  .page{position:absolute;top:99px;width:496px;height:701px;background:#fff;overflow:hidden}
  .page--cover{left:82px}
  .page--overview{left:622px;background:#f7fafa}
  .page-bg{position:absolute;inset:0;width:100%;height:100%}

  /* cover */
  .brand{position:absolute;left:28px;top:58px;display:flex;align-items:center;gap:7px;
    font:700 20px/1 'Oswald',sans-serif;color:var(--title-teal);letter-spacing:.5px}
  .brand-dot{width:14px;height:14px;border-radius:50%;background:var(--green)}
  .cover-title{position:absolute;left:116px;top:232px;font-family:'Oswald',sans-serif;font-weight:700;line-height:1}
  .cover-title .t1{display:block;font-size:54px;color:var(--grey-light);letter-spacing:1px}
  .cover-title .t2{display:block;font-size:74px;color:var(--grey-dark);margin-top:-2px;letter-spacing:1px}
  .cover-title .t3{display:block;font-size:38px;color:var(--title-teal);margin-top:0;letter-spacing:.5px}
  .cover-sub{position:absolute;left:38px;top:420px;font:700 17.5px/22px 'Roboto Condensed',sans-serif;color:var(--sub-green)}
  .cover-photo{position:absolute;left:104px;top:489px;width:168px;height:168px;border-radius:50%;
    background:var(--deep-teal);padding:6px}
  .cover-photo .photo{width:100%;height:100%;border-radius:50%;
    background:radial-gradient(circle at 50% 45%,#d9c6b4,#a89482 60%,#7d6c5e)}
  .author{position:absolute;right:30px;top:583px;text-align:right;color:#fff;font-family:'Oswald',sans-serif}
  .author .name{font-size:24px;font-weight:700;line-height:1;letter-spacing:.5px}
  .author .date{font-family:'Roboto Condensed',sans-serif;font-weight:700;font-size:15px;margin-top:3px;padding-right:22px}

  /* overview */
  .section-head{position:absolute;font:700 17px/1 'Oswald',sans-serif;color:#3d3d3d;letter-spacing:.5px}
  .overview-head{left:26px;top:27px}
  .summary{position:absolute;left:24px;top:46px;width:448px;height:113px;background:var(--summary-bg);
    color:#fff;font:400 8.7px/11.2px 'Roboto',sans-serif;padding:6px 10px}
  .stats{position:absolute;left:41px;top:170px;display:flex;gap:12px}
  .stat{width:95px;height:59px;background:var(--stat-foot)}
  .stat-value{height:23px;color:#fff;font:700 15px/23px 'Oswald',sans-serif;text-align:center;letter-spacing:.5px}
  .stat-label{font:700 5.8px/7px 'Roboto Condensed',sans-serif;color:#6a6a6a;text-align:center;padding:8px 6px 0;text-transform:uppercase}
  .stat--green .stat-value{background:var(--stat-green)}
  .stat--olive .stat-value{background:var(--stat-olive)}
  .stat--teal .stat-value{background:var(--stat-teal)}
  .stat--sky .stat-value{background:var(--stat-sky)}
  .meaning-q{position:absolute;left:47px;top:236px;font:400 11.5px/1 'Roboto Condensed',sans-serif;color:#333}
  .meaning{position:absolute;left:82px;top:254px;width:360px;list-style:none;font:400 8.8px/10.5px 'Roboto',sans-serif;color:var(--ink)}
  .meaning li{position:relative;padding-left:17px;margin-bottom:7px}
  .meaning .cycle{position:absolute;left:0;top:0;width:12px;height:12px}
  .meaning .callout{color:var(--sub-green);font-weight:700;padding-left:53px;margin-top:5px}
  .col{position:absolute;top:383px;width:204px;font:400 8.8px/11.3px 'Roboto',sans-serif;color:var(--ink);text-align:justify}
  .col p{margin-bottom:8px}
  .col strong{color:#333}
  .col--left{left:34px}
  .col--right{left:258px}
  .baseline-head{font:700 11px/1 'Oswald',sans-serif;color:#3d3d3d;margin:12px 0 8px;letter-spacing:.3px}
  .what{font:700 11px/1 'Roboto',sans-serif;color:#333;margin-bottom:6px}
  .problems{list-style:none}
  .problems li{position:relative;padding-left:10px;margin-bottom:4px;text-align:left}
  .problems li::before{content:"";position:absolute;left:0;top:3px;width:5px;height:5px;border:1px solid #555;border-radius:50%}
  sup{font-size:5.5px;color:var(--blue)}
</style>
</head>
<body>
<main class="spread">

  <section class="page page--cover">
    <svg class="page-bg" viewBox="0 0 496 701" aria-hidden="true">
      <polygon points="0,0 308,0 0,300" fill="#c9d9de"/>
      <polygon points="80,0 308,0 160,120" fill="#d8e4e7"/>
      <polygon points="496,0 496,180 380,60" fill="#eaf5f8"/>
      <polygon points="0,512 188,701 0,701" fill="var(--sky)"/>
      <polygon points="0,560 140,701 0,701" fill="#9fd6e2"/>
      <polygon points="496,393 496,701 188,701" fill="var(--deep-teal)"/>
      <polygon points="496,470 496,701 260,701" fill="#348fa4"/>
    </svg>
    <div class="brand"><span class="brand-dot"></span>TELVARIS-QP</div>
    <h1 class="cover-title">
      <span class="t1">CHANGING</span>
      <span class="t2">PHARMA’S</span>
      <span class="t3">PARADIGM OF WASTE</span>
    </h1>
    <p class="cover-sub">How Pharma's Demand Volatility<br>Could Be Costing You Millions in<br>Material Write-downs &amp; Procurement</p>
    <div class="cover-photo"><div class="photo" role="img" aria-label="Portrait photo of a smiling baby in a knitted hood"></div></div>
    <div class="author"><div class="name">DANA MORROW</div><div class="date">August 2018</div></div>
  </section>

  <section class="page page--overview">
    <svg class="page-bg" viewBox="0 0 496 701" aria-hidden="true">
      <polygon points="120,0 300,0 210,120" fill="#f0f1e4"/>
      <polygon points="300,0 496,0 496,160" fill="#e3f2f5"/>
      <polygon points="100,150 250,380 0,380 0,260" fill="#eef2e8" opacity=".7"/>
      <polygon points="496,390 496,701 290,701" fill="var(--pale-sky)"/>
      <polygon points="0,440 180,701 0,701" fill="#d6ecf1"/>
      <polygon points="200,560 310,701 150,701" fill="#e6f3f6"/>
    </svg>
    <h2 class="section-head overview-head">OVERVIEW</h2>
    <p class="summary">Demand volatility is a challenge for very supply chain.&nbsp; It strikes at the end of supply chains causing a "bullwhip effect" that becomes exponentially more impactful further back in the chain.&nbsp; For Pharma, the effect is strongest in manufacturing and procurement, specifically with starting raw materials and consumables. Swings in demand can cripple launches, cause stock-outs, inflate material prices, make lean planning ineffective, and cause significant write-downs of residual/obsolete materials; ultimately inflating CoGS and reducing net income.&nbsp; These swings can also cause inventory costs to inflate, materials to expire or become obsolete, higher disposal fees, and a larger carbon footprint.The yearly financial impacts are staggering considering Pharma's economic footprint. Twenty of Pharma's top 100 companies were sampled using 2015 &amp; 2016 financial figures1-2-3-4.&nbsp; Industry estimates for waste include:</p>

    <div class="stats">
      <div class="stat stat--green"><div class="stat-value">3.77%</div><div class="stat-label">Avg raw material write-down as a % of net income</div></div>
      <div class="stat stat--olive"><div class="stat-value">$ 2.7 B</div><div class="stat-label">Est pharma written down inventory in 2016</div></div>
      <div class="stat stat--teal"><div class="stat-value">$ 2,034</div><div class="stat-label">Est US pharma revenue per 1 ton non-MSW waste</div></div>
      <div class="stat stat--sky"><div class="stat-value">.01</div><div class="stat-label">Correlation coefficient of material write-downs and firm size</div></div>
    </div>

    <p class="meaning-q">What do these numbers mean?</p>
    <ul class="meaning">
      <li><svg class="cycle" viewBox="0 0 12 12"><path d="M10 6a4 4 0 1 1-1.2-2.8" fill="none" stroke="var(--stat-green)" stroke-width="2"/><path d="M7 1.5h3v3z" fill="var(--stat-green)"/></svg>3.77% is an alarmingly high, and does not include capitalized consumables, equipment disposal, and similar wastes
        <div class="callout">$5B in net income LS Firm: est $185M in write-downs<br>$50M in net income LS Firm: est $1.9M in write-downs</div></li>
      <li><svg class="cycle" viewBox="0 0 12 12"><path d="M10 6a4 4 0 1 1-1.2-2.8" fill="none" stroke="var(--stat-olive)" stroke-width="2"/><path d="M7 1.5h3v3z" fill="var(--stat-olive)"/></svg>$2.7B is likely much lower than the real figure due to capitalizing consumable inventories for launches etc.</li>
      <li><svg class="cycle" viewBox="0 0 12 12"><path d="M10 6a4 4 0 1 1-1.2-2.8" fill="none" stroke="var(--stat-teal)" stroke-width="2"/><path d="M7 1.5h3v3z" fill="var(--stat-teal)"/></svg>$2,034 to one ton of industrial waste is not progressive.</li>
      <li><svg class="cycle" viewBox="0 0 12 12"><path d="M10 6a4 4 0 1 1-1.2-2.8" fill="none" stroke="var(--stat-sky)" stroke-width="2"/><path d="M7 1.5h3v3z" fill="var(--stat-sky)"/></svg>.01 correlation coefficient means this problem does not discriminate based on company size and is ubiquitous in the industry.</li>
    </ul>

    <div class="col col--left">
      <p>Industries have attempted to mitigate the bullwhip effect through many techniques and systems such as ERP, robust forecasting models, demand management, LSS tools, strategic sourcing, etc. However, life science firms still struggle to effectively address this problem as evidenced by the write-down figures.&nbsp; Many non-FDA regulated industries have started utilizing marketplaces and brokerage services to create circular supply chains that optimize waste by connecting buyers and sellers. However, Pharma and life sciences have yet to adopt this waste-centric supply chain and execute it in a manner conducive to the compliance and indemnification requirements of the industry regarding primary and secondary transactions of raw materials, equipment, consumables, spare parts, and collaborative relationships.&nbsp; Finished products such as APIs, intermediates, and devices are out of scope for this supply chain.</p>
      <p><strong>A life sciences marketplace and consortium</strong> for manufacturuers, reserachers, and vendors canminimize the aforementioned problems by quickly, innovatively, and transparently exchanging material information in safe and controlled environment ensuring a firm's standards for data</p>
    </div>

    <div class="col col--right">
      <p>integrity, cGMP compliance, contractual indemnification, and financial benefits are met; all by leveraging core auditing skills.</p>
      <p>It is a call to arms among supply chain, procurement, and quality leaders to take part in a more circular, greener, and collaborative supply chain.Time is critical as global competition grows, customer and government emphasis on lowering pricing mounts<sup>5</sup>, and collective pressure on sustainability demands widespread action.</p>
      <p>Let's explore Current and Future State of this industry issue to understand why such a marketplace can begin the much-needed transition for life science companies.</p>
      <h3 class="baseline-head">BASELINE PROBLEM</h3>
      <p class="what">What?</p>
      <ul class="problems">
        <li>Disposal of high quality materials, equipment, spare parts</li>
        <li>Single and/or limited sources of supply</li>
        <li>Inability to collaborative with like-minded life sciences firms</li>
      </ul>
    </div>
  </section>

</main>
</body>
</html>
```